Business cards for Norwegian software consultancy business

We are in need of business cards for our Norwegian consultancy company.
“Talvik Brensor AS” specializes in software development, architecture and agile methodology, providing mostly on-site services at customers.
The cards should reflect a certain level of business professionalism with an elegant touch, while paying tribute to our modern and technological heritage. Our logo should be featured, as well as room for basic information about the cardholder and legal information of the company (company name, address and VAT number).
We would like our cards to reflect that we are a modern consulting company. It should present a professional image that people will remember. The texture and color pallette should reflect our professionalism and reliability, so we prefer a light color pallette with colors such as gray, white, blue and black. The number of colors used should however not be overwhelming, with the text being distinct and readable.
We are open to untraditional layouts and playful designs as long as they communicate the intent stated above.
You could also take a look at our website http://www.brensor.no for input on our visual profile.
Our logo is attached in the form of vectors and rasterized PNG. Please comment if you would like the black-white and/or inverted versions as well.
Architecture
Company information:
Talvik Brensor AS
Lindeholtveien 7, 3142 Vestskogen
461 82 915
info@brensor.no
www.brensor.no
Employee information:
Full name
Title
Email
Phone

```html
<!DOCTYPE html>
<html lang="en">
<head>
<meta charset="utf-8">
<title>Talvik Brensor AS – Business Cards</title>
<link href="https://fonts.googleapis.com/css2?family=Lato:wght@400;700&display=swap" rel="stylesheet">
<style>
  :root {
    --stage: #2b2b2d;
    --card-dark: #3a3b3d;
    --card-light: #fbfbfb;
    --ink: #1c1c1c;
    --ink-soft: #3a3a3a;
    --blue: #3d8fce;
    --grey-light: #e9e9e9;
    --grey-mid: #b9b9b9;
  }
  * { box-sizing: border-box; margin: 0; padding: 0; }
  html, body {
    width: 1200px; height: 873px; overflow: hidden;
    background: var(--stage);
    font-family: "Lato", sans-serif;
  }
  .stage {
    position: relative; width: 1200px; height: 873px;
    display: flex; align-items: center; justify-content: center; gap: 50px;
  }
  .card {
    position: relative; width: 525px; height: 300px;
    border-radius: 16px; overflow: hidden;
    box-shadow: 0 14px 30px rgba(0,0,0,.45);
  }

  /* Back side */
  .card--back {
    background: var(--card-dark);
    display: flex; flex-direction: column; align-items: center; justify-content: center;
  }
  .brand { display: flex; align-items: center; gap: 14px; }
  .brand__mark { width: 22px; height: 22px; background: var(--blue); }
  .brand__name {
    font-weight: 400; letter-spacing: 3px; text-transform: uppercase;
  }
  .card--back .brand__name { font-size: 40px; color: var(--grey-light); }
  .tagline {
    margin-top: 34px; font-size: 12px; letter-spacing: 4.5px;
    color: var(--grey-mid); text-transform: uppercase;
  }

  /* Front side */
  .card--front { background: var(--card-light); color: var(--ink); }
  .front__brand {
    position: absolute; top: 34px; right: 34px;
    display: flex; flex-direction: column; align-items: flex-end;
  }
  .front__brand .brand { gap: 10px; }
  .front__brand .brand__mark { width: 14px; height: 14px; }
  .front__brand .brand__name { font-size: 24px; color: var(--ink); letter-spacing: 2px; }
  .vat { margin-top: 6px; font-size: 10px; font-weight: 700; color: var(--ink); }
  .divider {
    position: absolute; left: 170px; right: 34px; top: 150px;
    height: 1.5px; background: var(--ink);
  }
  .holder { position: absolute; left: 34px; top: 136px; }
  .holder__name { font-size: 17px; font-weight: 700; color: var(--blue); }
  .holder__title { font-size: 12px; color: var(--ink-soft); margin-top: 2px; }
  .contacts { list-style: none; margin-top: 18px; }
  .contacts li {
    display: flex; align-items: center; gap: 10px;
    font-size: 12px; font-weight: 700; color: var(--ink-soft); margin-bottom: 9px;
  }
  .contacts svg { width: 14px; height: 14px; flex: none; }
  .company {
    position: absolute; right: 34px; top: 164px; text-align: right;
  }
  .company__name { font-size: 14px; color: var(--ink); letter-spacing: .5px; }
  .company__name strong { font-weight: 700; }
  .company__address { font-size: 11.5px; color: var(--blue); margin-top: 4px; }
</style>
</head>
<body>
<main class="stage">

  <section class="card card--back" aria-label="Card back">
    <div class="brand">
      <span class="brand__mark"></span>
      <span class="brand__name">Talvik Brensor</span>
    </div>
    <p class="tagline">Development &amp; IT Services</p>
  </section>

  <section class="card card--front" aria-label="Card front">
    <div class="front__brand">
      <div class="brand">
        <span class="brand__mark"></span>
        <span class="brand__name">Talvik Brensor</span>
      </div>
      <p class="vat">VAT 917 604 382</p>
    </div>

    <div class="divider"></div>

    <div class="holder">
      <p class="holder__name">Henrik Solvang</p>
      <p class="holder__title">Owner / Founder</p>
      <ul class="contacts">
        <li>
          <svg viewBox="0 0 14 14" aria-hidden="true"><rect x="3.5" y="1" width="7" height="12" rx="1.5" fill="none" stroke="var(--blue)" stroke-width="1.4"/><circle cx="7" cy="11" r=".8" fill="var(--blue)"/></svg>
          +47 461 82 915
        </li>
        <li>
          <svg viewBox="0 0 14 14" aria-hidden="true"><rect x="1" y="3" width="12" height="8.5" fill="var(--blue)"/><path d="M1 3 L7 8 L13 3" fill="none" stroke="#fff" stroke-width="1.1"/></svg>
          info@brensor.no
        </li>
        <li>
          <svg viewBox="0 0 14 14" aria-hidden="true"><g fill="none" stroke="var(--blue)" stroke-width="1.5" stroke-linecap="round"><path d="M6 8 L8 6"/><path d="M5 6.5 L3 8.5 a2 2 0 0 0 2.5 2.5 L7.5 9"/><path d="M9 7.5 L11 5.5 a2 2 0 0 0 -2.5 -2.5 L6.5 5"/></g></svg>
          www.brensor.no
        </li>
      </ul>
    </div>

    <div class="company">
      <p class="company__name">TALVIK <strong>BRENSOR AS</strong></p>
      <p class="company__address">Lindeholtveien 7, 3142 Vestskogen, Norway</p>
    </div>
  </section>

</main>
</body>
</html>
```